Thornwell Building Company - advertisement poster

I am looking to print some canvas signs to advertise my general contracting company, Thornwell Building Company. The sign will measure 6' long x 3' high so the size should match that ratio. I already have a logo icon, which is the Letter 'A' and some trees that I would like to incorporate, see attached. I would also like the to have the following information listed:
1) phone number: 472-318-6095
2) email: thornwellbuildingcompany@mailvistra.net
3) website: thornwellbuildingcompany.com
4) Lic#5386204
5) I want to use this text: "BUILD WITH THE T-CREW!"

The ad should be relatively simple and clean. Black and Green are my company colors. I am open to creative ideas!

Target Market(s)

People looking to renovate their homes

Industry/Entity Type

Construction

Colors
59FF00
82FF00
B8FF75
E3FFCB
F4FFEA

Requirements
Must have
• Must have my company logo
Should not have
• No photos or complex graphics

```html
<!DOCTYPE html>
<html lang="en">
<head>
<meta charset="utf-8">
<title>Thornwell Building Company – Sign</title>
<link rel="stylesheet" href="https://fonts.googleapis.com/css2?family=Bebas+Neue&family=Nunito:wght@900&family=Arimo:wght@400&display=swap">
<style>
  :root {
    --page-bg: #e1ecc8;
    --forest: #22351f;
    --leaf: #6fb345;
    --paper: #ffffff;
    --mint: #e3eecb;
    --mint-light: #f4f9ea;
    --ink: #222222;
    --dot-grey: #e4e4e4;
  }
  html, body {
    margin: 0;
    padding: 0;
    width: 1200px;
    height: 1200px;
    overflow: hidden;
    background: var(--page-bg);
  }
  .sign {
    position: absolute;
    left: 49px;
    top: 324px;
    width: 1103px;
    height: 552px;
    display: block;
  }
  .headline {
    font-family: "Bebas Neue", "Oswald", sans-serif;
    font-size: 200px;
  }
  .headline-green { fill: var(--leaf); }
  .headline-dark { fill: var(--forest); }
  .phone {
    font-family: "Nunito", "Arial Rounded MT Bold", sans-serif;
    font-weight: 900;
    font-size: 158px;
    fill: var(--paper);
  }
  .brand-name {
    font-family: "Bebas Neue", "Oswald", sans-serif;
    fill: var(--paper);
  }
  .contact {
    font-family: "Arimo", "Helvetica", "Arial", sans-serif;
    font-size: 38px;
    fill: var(--ink);
  }
</style>
</head>
<body>
<svg class="sign" viewBox="0 0 1775 888" xmlns="http://www.w3.org/2000/svg">
  <defs>
    <linearGradient id="texture-left" x1="0" y1="0" x2="1" y2="1">
      <stop offset="0" stop-color="var(--dot-grey)" stop-opacity="1"/>
      <stop offset="1" stop-color="var(--paper)" stop-opacity="0"/>
    </linearGradient>
    <linearGradient id="texture-right" x1="1" y1="0" x2="0" y2="1">
      <stop offset="0" stop-color="var(--dot-grey)" stop-opacity="1"/>
      <stop offset="1" stop-color="var(--paper)" stop-opacity="0"/>
    </linearGradient>
  </defs>

  <!-- sign body -->
  <rect class="sign-face" x="0" y="0" width="1775" height="888" fill="var(--paper)"/>

  <!-- corner textures -->
  <rect class="texture" role="img" aria-label="Soft grey dotted texture" x="0" y="0" width="420" height="320" fill="url(#texture-left)"/>
  <rect class="texture" role="img" aria-label="Soft grey dotted texture" x="1355" y="0" width="420" height="340" fill="url(#texture-right)"/>

  <!-- side accent blocks -->
  <polygon class="side-accent" points="417,0 517,0 517,263 287,263" fill="var(--leaf)"/>
  <polygon class="side-accent" points="1270,0 1370,0 1500,263 1270,263" fill="var(--leaf)"/>

  <!-- crest -->
  <polygon class="crest-rim" points="534,0 1252,0 1252,263 1000,338 890,342 786,338 534,263" fill="var(--leaf)"/>
  <polygon class="crest-gap" points="556,0 1230,0 1230,256 890,368 556,256" fill="var(--paper)"/>
  <polygon class="crest" points="572,0 1214,0 1214,248 890,370 572,248" fill="var(--forest)"/>

  <!-- brand block -->
  <rect class="brand-mark" role="img" aria-label="Company logo mark" x="840" y="56" width="100" height="100" fill="var(--leaf)"/>
  <text class="brand-name" x="890" y="230" text-anchor="middle" font-size="68" textLength="450" lengthAdjust="spacingAndGlyphs">THORNWELL</text>
  <text class="brand-name" x="890" y="261" text-anchor="middle" font-size="27" textLength="447" lengthAdjust="spacing">BUILDING COMPANY</text>

  <!-- headline -->
  <text class="headline" x="887" y="551" text-anchor="middle" textLength="1480" lengthAdjust="spacingAndGlyphs"><tspan class="headline-green">BUILD WITH THE </tspan><tspan class="headline-dark">T-CREW!</tspan></text>

  <!-- phone band -->
  <rect class="phone-band" x="0" y="598" width="1775" height="160" fill="var(--forest)"/>
  <polygon class="phone-plate" points="377,615 1447,615 1387,771 317,771" fill="var(--leaf)"/>
  <text class="phone" x="887" y="741" text-anchor="middle" textLength="900" lengthAdjust="spacingAndGlyphs">472-318-6095</text>

  <!-- contact strip -->
  <rect class="contact-strip" x="0" y="758" width="1775" height="130" fill="var(--mint)"/>
  <polygon class="contact-highlight" points="827,758 1492,758 1447,888 784,888" fill="var(--mint-light)"/>

  <g class="icon-mail">
    <rect x="44" y="818" width="38" height="28" rx="3" fill="var(--leaf)"/>
    <polyline points="46,821 63,835 80,821" fill="none" stroke="var(--mint)" stroke-width="3"/>
  </g>
  <text class="contact" x="97" y="845" textLength="672" lengthAdjust="spacingAndGlyphs">thornwellbuildingcompany@mailvistra.net</text>

  <g class="icon-globe" fill="none" stroke="var(--leaf)" stroke-width="3">
    <circle cx="844" cy="831" r="16" fill="var(--leaf)" stroke="none"/>
    <ellipse cx="844" cy="831" rx="7" ry="16" stroke="var(--mint-light)"/>
    <line x1="828" y1="831" x2="860" y2="831" stroke="var(--mint-light)"/>
  </g>
  <text class="contact" x="882" y="845" textLength="548" lengthAdjust="spacingAndGlyphs">thornwellbuildingcompany.com</text>

  <text class="contact" x="1502" y="845" textLength="223" lengthAdjust="spacingAndGlyphs">Lic#5386204</text>
</svg>
</body>
</html>
```